We have built a site at brightpocketgadgets.example, but it is missing several elements and several don't work. I even like the color scheme we have. I do not know to do too much with code so if there is anything I need to do, it must be very minimal.

We essentially want what is there with:

1) a small column on the left side for categories, which are currently bottom right
2) space for a 728-90 banner ad at the top under the menu below the logo
3) drop down menus under the top logo that actually work
4) the top menu (where we have ages), the logo, the drop down menus and the 728-90 banner all need to space together neatly
5) the top logo needs to center
6) under the title of each post on the home page it says "comment and reactions." I'd like reactions removed since I have no idea what they are.
7) must be able to accept all widgets
8) I need a simple way to access the code to the top banner ad when it is placed to change as needed

That's about it other than any suggestions to make it better. I like clean and simple in blog format.
Updates

Sorry I should have mentioned that we want the text of the categories smaller so that can fit in a smaller left column. I'd have to see but I'd guess about 10 point.

Industry/Entity Type

Work

Requirements
Must have
• see above

```html
<!DOCTYPE html>
<html lang="en">
<head>
<meta charset="utf-8">
<title>Bright Pocket Gadgets</title>
<link rel="stylesheet" href="https://fonts.googleapis.com/css2?family=Arimo:wght@400;700&family=Montserrat:wght@500;600&family=Oswald:wght@500;600&family=Open+Sans:ital,wght@1,700&display=swap">
<style>
:root{
  --wood:#3a2f29;
  --cream:#f5f0e4;
  --green:#5aa31a;
  --green-light:#8fd13a;
  --green-dark:#3e7d0c;
  --ink:#1d1d1d;
  --text:#555;
  --muted:#888;
  --rule:#e4e4e4;
  --orange:#e35d0c;
  --red:#d62a12;
  --banner-a:#ffd46a;
  --banner-b:#f59a12;
  --social:#2aa7dc;
}
*{margin:0;padding:0;box-sizing:border-box}
html,body{width:847px;height:1200px;overflow:hidden;background:#fff}
body{font-family:"Arimo",Arial,sans-serif;color:var(--text);position:relative}
.abs{position:absolute}

.age-bar{left:0;top:0;width:847px;height:22px;background:var(--wood);display:flex;justify-content:center;gap:18px;align-items:center}
.age-bar a{color:#f2ede4;font:500 10.5px "Montserrat",sans-serif;text-decoration:none;letter-spacing:.4px}

.masthead{left:0;top:22px;width:847px;height:163px;background:var(--cream)}
.brand{left:0;top:30px;width:847px;height:42px;display:flex;justify-content:center;align-items:center;gap:12px}
.brand-dot{width:30px;height:30px;border-radius:50%;background:var(--green)}
.brand-name{font:600 36px/42px "Oswald",sans-serif;color:var(--wood);letter-spacing:1.5px;text-transform:uppercase}
.slab{left:146px;top:76px;width:555px;height:22px;background:var(--wood);border-radius:3px}
.slab span{display:block;color:var(--cream);font:500 10px/22px "Montserrat",sans-serif;text-align:center;letter-spacing:2px}

.ad-banner{left:182px;top:112px;width:482px;height:59px;background:linear-gradient(180deg,var(--banner-a),var(--banner-b));border:1px solid #e08a10;display:flex;align-items:center;padding-left:14px;gap:10px}
.ad-mark{width:28px;height:28px;background:#4d4d4d;border-radius:4px}
.ad-brand{font:600 20px "Montserrat",sans-serif;color:#fff;background:#3c3c3c;padding:4px 10px;border-radius:3px}
.ad-copy{margin-left:18px;font:600 30px "Oswald",sans-serif;color:#fff}
.ad-copy b{color:#5a2a00;font-weight:600}

.main-nav{left:0;top:185px;width:847px;height:24px;background:linear-gradient(180deg,var(--green-light),var(--green));border-bottom:2px solid var(--green-dark)}
.main-nav ul{list-style:none;display:flex;margin-left:120px;height:100%}
.main-nav li{height:100%;padding:0 21px;display:flex;align-items:center;font:italic 700 11.5px "Open Sans",sans-serif;color:#fff}
.main-nav li.is-current{background:var(--green-dark);padding:0 24px}
.nav-shade{left:0;top:211px;width:847px;height:30px;background:linear-gradient(180deg,#f3f3f3,#fff)}

.widget-head{height:27px;display:flex;align-items:center;background:var(--wood);color:#fff;font:500 13px "Oswald",sans-serif;letter-spacing:.3px;clip-path:polygon(0 0,92% 0,100% 100%,0 100%)}
.widget-head i{width:18px;height:27px;background:var(--green);margin-right:9px;position:relative}
.widget-head i::after{content:"";position:absolute;left:6px;top:10px;border:4px solid transparent;border-left:5px solid #fff}

.categories{left:100px;top:242px;width:131px;height:832px;border:1px solid var(--rule);border-top:none}
.categories .widget-head{margin:0 -1px}
.cat-list{list-style:none;padding:10px 0 0 9px}
.cat-list li{font-size:8.3px;line-height:16.45px;color:var(--muted);white-space:nowrap}
.cat-list li.sub{padding-left:7px}
.cat-list li.active{color:var(--red)}

.posts{left:251px;top:238px;width:312px}
.post{height:228px;position:relative}
.post::after{content:"";position:absolute;left:0;top:204px;width:312px;height:2px;background:#eee}
.post-title{font:500 15.5px "Montserrat",sans-serif;color:var(--ink);height:28px;padding-top:2px}
.post-body{display:flex;gap:13px}
.post-thumb{width:130px;height:130px;border:3px solid #e9e9e9;flex:none}
.post-thumb div{width:100%;height:100%}
.post-excerpt{font-size:10.4px;line-height:16.5px;color:var(--text);margin-top:-3px}
.post-excerpt a{color:var(--orange);font-weight:700;font-size:9.5px;text-decoration:none}
.post-meta{position:absolute;left:0;top:168px;width:312px;display:flex;align-items:center;font-size:8.6px;color:var(--muted)}
.post-meta > span{display:flex;align-items:center;gap:6px}
.post-meta .date{width:82px}
.post-meta .comments{width:88px}
.post-meta .author{width:91px}
.post-meta .share{display:flex;gap:10px;margin-left:auto}
.share i{width:7px;height:7px;border-radius:50%;background:var(--social)}
.ico{width:8px;height:8px;flex:none}

.sidebar{left:582px;top:242px;width:166px}
.search{display:flex;height:18px}
.search div{flex:1;border:1px solid var(--rule);font-size:8px;color:var(--muted);padding:4px 6px;font-weight:700}
.search button{width:24px;background:var(--wood);border:none;border-radius:0 3px 3px 0;display:flex;align-items:center;justify-content:center}
.alert-title{margin-top:16px;font:600 14px "Montserrat",sans-serif;color:var(--ink)}
.alert-sub{font-size:9.5px;color:var(--ink);margin-top:2px}
.alert-form{display:flex;margin-top:9px;height:17px}
.alert-form div{flex:1;border-bottom:1px solid var(--rule);font-size:8px;color:var(--muted);padding:3px 6px;font-weight:700}
.alert-form span{width:44px;background:linear-gradient(180deg,var(--green-light),var(--green));color:#fff;font-size:9.5px;font-weight:700;text-align:center;line-height:17px;border-radius:2px}
.side-box{border:1px solid var(--rule);border-top:none}
.side-box .widget-head{margin:0 -1px}
.developers{margin-top:21px}
.developers p{font-size:9.5px;line-height:16.5px;color:var(--ink);padding:7px 9px 12px}
.popular{margin-top:20px}
.popular ul{list-style:none;padding:6px 10px 8px}
.popular li{font-size:8.5px;line-height:16.5px;color:var(--muted)}
.promo{margin-top:21px;width:166px;height:165px;position:relative;background:linear-gradient(160deg,#0b5f7a,#3d8fa8 45%,#a6b89a)}
.promo span{position:absolute;left:0;bottom:0;background:rgba(0,0,0,.55);color:#fff;font-size:9px;font-weight:700;padding:3px 5px}

.footer{left:0;top:1162px;width:847px;height:38px;background:var(--wood)}
.footer-links{position:absolute;left:99px;top:7px;font-size:8.5px;font-weight:700;color:#f2ede4}
.footer-copy{position:absolute;left:99px;top:22px;font-size:8.5px;color:#f2ede4}
.footer-social{position:absolute;left:672px;top:11px;display:flex;gap:12px}
.footer-social i{width:16px;height:16px;border-radius:50%;background:#f2ede4}
</style>
</head>
<body>

<nav class="abs age-bar">
  <a>AGES 1-2 (TODDLER)</a><a>AGES 3-4 (PRE SCHOOL)</a><a>AGES 5-6</a><a>AGES 7-8</a><a>AGES 9-10</a>
</nav>

<header class="abs masthead"></header>
<div class="abs brand"><span class="brand-dot"></span><span class="brand-name">Bright Pocket Gadgets</span></div>
<div class="abs slab"><span>BRIGHTPOCKETGADGETS.EXAMPLE</span></div>

<div class="abs ad-banner">
  <span class="ad-mark"></span>
  <span class="ad-brand">markupmill</span>
  <span class="ad-copy">PSD to XHTML <b>$45</b></span>
</div>

<nav class="abs main-nav">
  <ul>
    <li class="is-current">Home</li><li>Best Free Apps</li><li>Free Apps</li><li>Best Apps</li><li>Submit App</li><li>Contact</li>
  </ul>
</nav>
<div class="abs nav-shade"></div>

<aside class="abs categories">
  <div class="widget-head"><i></i>APP CATEGORIES</div>
  <ul class="cat-list">
    <li class="active">Addition (2)</li>
    <li class="sub">Best free apps</li>
    <li class="sub">Colors</li>
    <li class="sub">Drawing (1)</li>
    <li class="sub">Engineering (1)</li>
    <li class="sub">English</li>
    <li>Ages 1-2 (toddler) (2)</li>
    <li>Ages 3-4 (preschool) (9)</li>
    <li>Ages 5-6 (7)</li>
    <li>Ages 7-8 (2)</li>
    <li>Ages 8-9 (1)</li>
    <li>Ages 9-10 (2)</li>
    <li>Alphabet/letters (3)</li>
    <li>Animals (1)</li>
    <li>Art (2)</li>
    <li>Best apps (3)</li>
    <li>Best free apps (2)</li>
    <li>Books (1)</li>
    <li>Coloring (1)</li>
    <li>Colors (1)</li>
    <li>Connect the dots (1)</li>
    <li>Drawing (1)</li>
    <li>Engineering (1)</li>
    <li>English (1)</li>
    <li>Food and drink (1)</li>
    <li>Free apps (4)</li>
    <li>Hand-eye coordination (2)</li>
    <li>Has in-app purchases (2)</li>
    <li>Has third-party ads (1)</li>
    <li>Health (1)</li>
    <li>Just for fun (1)</li>
    <li>Matching (2)</li>
    <li>Math (3)</li>
    <li>Mazes (1)</li>
    <li>Music (1)</li>
    <li>Numbers/counting (3)</li>
    <li>Patterns (2)</li>
    <li>Phonics (1)</li>
    <li>Puzzles (1)</li>
    <li>Reading, sentences (1)</li>
    <li>Reading, words (1)</li>
    <li>Role-playing (1)</li>
    <li>Science (1)</li>
    <li>Social studies (1)</li>
    <li>Sorting (1)</li>
    <li>Subtraction (2)</li>
    <li>Tech (1)</li>
    <li>Uncategorized (5)</li>
  </ul>
</aside>

<main class="abs posts">
  <article class="post">
    <h2 class="post-title">Proin gravida nibh vel velit aucto.</h2>
    <div class="post-body">
      <figure class="post-thumb"><div role="img" aria-label="Screenshot of a weather and clock widget app" style="background:linear-gradient(160deg,#4aa8e0,#123a6a 55%,#0a1630)"></div></figure>
      <p class="post-excerpt">Lorem Ipsum. Proin gravida nibh vel velit auctor aliquet. Aenean sollicitudin, lorem quis bibendum auctor, nisi elit consequat ipsum, sagittis sem nibh id elit. Lorem Ipsum. Proin gravida nibh vel velit auctor aliquet. <a>Read More</a></p>
    </div>
    <div class="post-meta">
      <span class="date"><svg class="ico" viewBox="0 0 8 8"><circle cx="4" cy="4" r="3.2" fill="none" stroke="#e35d0c" stroke-width="1.2"/><path d="M4 2.2V4h1.5" stroke="#e35d0c" fill="none"/></svg>21 APR 2013</span>
      <span class="comments"><svg class="ico" viewBox="0 0 8 8"><path d="M0 0h8v6H3L1 8V6H0z" fill="#e35d0c"/></svg><span>Comment (<b>10</b>)</span></span>
      <span class="author"><svg class="ico" viewBox="0 0 8 8"><circle cx="4" cy="2.3" r="2" fill="#e35d0c"/><path d="M0 8c0-3 8-3 8 0z" fill="#e35d0c"/></svg>Admin</span>
      <span class="share" aria-label="Share links"><i></i><i></i><i></i></span>
    </div>
  </article>

  <article class="post">
    <h2 class="post-title">Aenean sollicitudin, lorem quis.</h2>
    <div class="post-body">
      <figure class="post-thumb"><div role="img" aria-label="Screenshots of a stopwatch and timer app" style="background:linear-gradient(160deg,#d9dde0,#5a6168 50%,#222)"></div></figure>
      <p class="post-excerpt">Lorem Ipsum. Proin gravida nibh vel velit auctor aliquet. Aenean sollicitudin, lorem quis bibendum auctor, nisi elit consequat ipsum, sagittis sem nibh id elit. Lorem Ipsum. Proin gravida nibh vel velit auctor aliquet. <a>Read More</a></p>
    </div>
    <div class="post-meta">
      <span class="date"><svg class="ico" viewBox="0 0 8 8"><circle cx="4" cy="4" r="3.2" fill="none" stroke="#e35d0c" stroke-width="1.2"/><path d="M4 2.2V4h1.5" stroke="#e35d0c" fill="none"/></svg>21 APR 2013</span>
      <span class="comments"><svg class="ico" viewBox="0 0 8 8"><path d="M0 0h8v6H3L1 8V6H0z" fill="#e35d0c"/></svg><span>Comment (<b>10</b>)</span></span>
      <span class="author"><svg class="ico" viewBox="0 0 8 8"><circle cx="4" cy="2.3" r="2" fill="#e35d0c"/><path d="M0 8c0-3 8-3 8 0z" fill="#e35d0c"/></svg>Admin</span>
      <span class="share" aria-label="Share links"><i></i><i></i><i></i></span>
    </div>
  </article>

  <article class="post">
    <h2 class="post-title">Duis sed odio sit amet nibh vulputate.</h2>
    <div class="post-body">
      <figure class="post-thumb"><div role="img" aria-label="Promotional tile for an office suite app" style="background:linear-gradient(180deg,#f4f4f4 0 16%,#2f7fc4 16%,#1a5aa0 70%,#e9a23a)"></div></figure>
      <p class="post-excerpt">Lorem Ipsum. Proin gravida nibh vel velit auctor aliquet. Aenean sollicitudin, lorem quis bibendum auctor, nisi elit consequat ipsum, sagittis sem nibh id elit. Lorem Ipsum. Proin gravida nibh vel velit auctor aliquet. <a>Read More</a></p>
    </div>
    <div class="post-meta">
      <span class="date"><svg class="ico" viewBox="0 0 8 8"><circle cx="4" cy="4" r="3.2" fill="none" stroke="#e35d0c" stroke-width="1.2"/><path d="M4 2.2V4h1.5" stroke="#e35d0c" fill="none"/></svg>21 APR 2013</span>
      <span class="comments"><svg class="ico" viewBox="0 0 8 8"><path d="M0 0h8v6H3L1 8V6H0z" fill="#e35d0c"/></svg><span>Comment (<b>10</b>)</span></span>
      <span class="author"><svg class="ico" viewBox="0 0 8 8"><circle cx="4" cy="2.3" r="2" fill="#e35d0c"/><path d="M0 8c0-3 8-3 8 0z" fill="#e35d0c"/></svg>Admin</span>
      <span class="share" aria-label="Share links"><i></i><i></i><i></i></span>
    </div>
  </article>

  <article class="post">
    <h2 class="post-title">Proin gravida nibh vel velit aucto.</h2>
    <div class="post-body">
      <figure class="post-thumb"><div role="img" aria-label="Screenshot of a weather and clock widget app" style="background:linear-gradient(160deg,#4aa8e0,#123a6a 55%,#0a1630)"></div></figure>
      <p class="post-excerpt">Lorem Ipsum. Proin gravida nibh vel velit auctor aliquet. Aenean sollicitudin, lorem quis bibendum auctor, nisi elit consequat ipsum, sagittis sem nibh id elit. Lorem Ipsum. Proin gravida nibh vel velit auctor aliquet. <a>Read More</a></p>
    </div>
    <div class="post-meta">
      <span class="date"><svg class="ico" viewBox="0 0 8 8"><circle cx="4" cy="4" r="3.2" fill="none" stroke="#e35d0c" stroke-width="1.2"/><path d="M4 2.2V4h1.5" stroke="#e35d0c" fill="none"/></svg>21 APR 2013</span>
      <span class="comments"><svg class="ico" viewBox="0 0 8 8"><path d="M0 0h8v6H3L1 8V6H0z" fill="#e35d0c"/></svg><span>Comment (<b>10</b>)</span></span>
      <span class="author"><svg class="ico" viewBox="0 0 8 8"><circle cx="4" cy="2.3" r="2" fill="#e35d0c"/><path d="M0 8c0-3 8-3 8 0z" fill="#e35d0c"/></svg>Admin</span>
      <span class="share" aria-label="Share links"><i></i><i></i><i></i></span>
    </div>
  </article>
</main>

<aside class="abs sidebar">
  <div class="search">
    <div>Search</div>
    <button aria-label="Search"><svg width="10" height="10" viewBox="0 0 10 10"><circle cx="4" cy="4" r="3" fill="none" stroke="#fff" stroke-width="1.5"/><path d="M6.2 6.2L9.5 9.5" stroke="#fff" stroke-width="1.8"/></svg></button>
  </div>
  <h3 class="alert-title">Pocketbot App Alert</h3>
  <p class="alert-sub">Subscribe to our Pocketbot Alert!</p>
  <div class="alert-form"><div>Email</div><span>Sign up</span></div>

  <section class="side-box developers">
    <div class="widget-head"><i></i>DEVELOPERS</div>
    <p>Send us your app info!<br>http://www.brightpocketkids.example/<br>welcome-pocketbot-developers.html</p>
  </section>

  <section class="side-box popular">
    <div class="widget-head"><i></i>MOST POPULAR POST</div>
    <ul><li>Most Commented</li><li>Most Viewed</li></ul>
  </section>

  <div class="promo" role="img" aria-label="Promotional photo of a person using a phone beneath a cloud of app icons"><span>Bright Pocket Gadgets Phones</span></div>
</aside>

<footer class="abs footer">
  <div class="footer-links">Best Free Apps &nbsp;|&nbsp; Free Apps &nbsp;|&nbsp; Best Apps &nbsp;|&nbsp; Submit App</div>
  <div class="footer-copy">© 2013 Bright Pocket Gadgets. All Rights Reserved | Privacy Statement</div>
  <div class="footer-social" aria-label="Social links"><i></i><i></i><i></i></div>
</footer>

</body>
</html>
```